依頼詳細
開店にはすこしまに合わないのですが、OPENチラシの作成をお願いいたします。

チラシ全体の雰囲気から癒しの雰囲気を感じ目にとまるデザインをお願いしたいです。

ある程度の構成は手書きで見にくくて申し訳ないのですが、添付しておりますので、
参考にして作って戴きたいです。

決してメニューの料金が安くないので、少し高級感も感じ、でも高級感がありすぎてチラシを見た方がハードルが高く感じていまわないようにしたいです。

記載項目
店名/住所/電話番号/QRコード/メニュー表/地図
サイズ
A4
ページ数
両面
希望イメージ
シンプル 複雑
単色 カラフル
暗い 明るい
日常 高級
遊び心 厳粛
未来的 伝統的
女性的 男性的
希望する色
青系
納品ファイル
• 高解像度JPG (.jpg)
• イラストレーター形式 (.ai)
補足説明
QRコードですが、まだ予約サイトが公開されておらず、10月28日公開予定で、URLをおくれるのが、28日以降になってしまいますので、その部分だけ余白であけておいて頂いて作成お願いします。28日以降に追加予約URLを添付いたします。
■ 選んだ理由

シンプルで見やすく全体的にバランスよくスッキリとまとまった印象を受け、
お客様がパッと見てもわかりやすいし目にとまるような気がしましたので、選ばせて戴きました。

■ 提案者全員のお礼・コメント

皆様この度は素敵なデザインのご提案戴き誠にありがとうございました。

また機会がございましたら、その際はよろしくお願いいたします。

```html
<!DOCTYPE html>
<html lang="ja">
<head>
<meta charset="utf-8">
<title>頭ほぐし専門店 soyo グランドオープン</title>
<link rel="stylesheet" href="https://fonts.googleapis.com/css2?family=Josefin+Sans:wght@600;700&family=Noto+Serif+JP:wght@400;500;600&family=Noto+Sans+JP:wght@400;500&display=swap">
<style>
  :root {
    --navy: #263a6b;
    --ink: #3a4560;
    --wash-blue: #bfe0ef;
    --wash-mint: #d6eedc;
    --wash-yellow: #f3efc4;
    --badge: #f2dd62;
    --accent: #3f8fc4;
    --paper: #fbfdfe;
  }
  * { margin: 0; padding: 0; box-sizing: border-box; }
  html, body { width: 854px; height: 1200px; overflow: hidden; background: var(--paper); }
  .flyer {
    position: relative; width: 854px; height: 1200px; overflow: hidden;
    font-family: "Noto Serif JP", serif; color: var(--navy);
  }
  .wash {
    position: absolute; inset: 0;
    background:
      radial-gradient(ellipse 420px 300px at 80% 12%, var(--wash-mint) 0%, transparent 70%),
      radial-gradient(ellipse 380px 260px at 15% 30%, var(--wash-blue) 0%, transparent 70%),
      radial-gradient(ellipse 460px 320px at 85% 55%, var(--wash-yellow) 0%, transparent 70%),
      radial-gradient(ellipse 520px 360px at 20% 78%, var(--wash-blue) 0%, transparent 72%),
      radial-gradient(ellipse 480px 300px at 80% 95%, var(--wash-mint) 0%, transparent 70%),
      var(--paper);
  }
  .headline {
    position: absolute; top: 112px; left: 0; width: 100%; text-align: center;
    font-family: "Josefin Sans", sans-serif; font-weight: 700; color: var(--navy);
    letter-spacing: 3px; line-height: 1.2;
  }
  .headline .date { font-size: 52px; }
  .headline .open { font-size: 60px; margin-top: 6px; }
  .coupon {
    position: absolute; left: 672px; top: 100px; width: 128px; height: 128px; border-radius: 50%;
    background: var(--badge); display: flex; align-items: center; justify-content: center;
    text-align: center; font-family: "Noto Sans JP", sans-serif; font-weight: 500;
    font-size: 15px; line-height: 1.45; color: var(--navy);
  }
  .symptoms {
    position: absolute; top: 360px; left: 0; width: 100%;
    display: flex; justify-content: center; gap: 14px;
  }
  .symptoms li {
    list-style: none; border: 1.5px solid var(--navy); padding: 6px 14px;
    font-family: "Noto Sans JP", sans-serif; font-size: 19px; background: rgba(255,255,255,.55);
  }
  .shop-type { position: absolute; top: 424px; width: 100%; text-align: center; font-size: 38px; font-weight: 600; letter-spacing: 4px; }
  .shop-kana { position: absolute; top: 476px; width: 100%; display: flex; justify-content: center; align-items: center; gap: 14px; font-size: 20px; letter-spacing: 6px; }
  .shop-kana::before, .shop-kana::after { content: ""; width: 110px; height: 1px; background: var(--navy); }
  .brand {
    position: absolute; top: 510px; width: 100%; text-align: center;
    font-family: "Josefin Sans", sans-serif; font-weight: 700; font-size: 120px; letter-spacing: 6px; line-height: 1;
  }
  .partner {
    position: absolute; top: 640px; width: 100%; text-align: center;
    font-family: "Josefin Sans", sans-serif; font-weight: 700; font-size: 34px; line-height: 1.1;
  }
  .partner .cross { display: block; font-size: 24px; }
  .tagline {
    position: absolute; top: 716px; left: 0; width: 100%; height: 58px;
    background: linear-gradient(90deg, rgba(255,255,255,0) 0%, rgba(255,255,255,.85) 20%, rgba(255,255,255,.85) 80%, rgba(255,255,255,0) 100%);
    text-align: center; font-size: 34px; font-weight: 500; line-height: 58px; letter-spacing: 3px;
  }
  .intro {
    position: absolute; top: 800px; left: 0; width: 100%; text-align: center;
    font-family: "Noto Sans JP", sans-serif; font-size: 15px; line-height: 2.05; color: var(--ink);
  }
  .intro p + p { margin-top: 4px; }
  .intro .mark { color: var(--accent); }
  .intro .closing { margin-top: 18px; }
</style>
</head>
<body>
<main class="flyer">
  <div class="wash" role="img" aria-label="淡い青・ミント・黄色の水彩背景"></div>

  <header class="headline">
    <div class="date">2021.11.1</div>
    <div class="open">GRAND<br>OPEN!!</div>
  </header>

  <div class="coupon">ご新規様<br>限定クーポン<br>配布中</div>

  <ul class="symptoms">
    <li>目の疲れ</li><li>頭痛</li><li>肩こり</li><li>だるさ</li>
  </ul>

  <p class="shop-type">頭ほぐし専門店</p>
  <p class="shop-kana">ソヨ</p>
  <h1 class="brand">soyo</h1>
  <p class="partner"><span class="cross">×</span>Lull</p>

  <p class="tagline">あなたの疲れに、極上の癒しを。</p>

  <section class="intro">
    <p>日常生活で抱えるストレスは、身体だけではなく<span class="mark">脳が疲労</span>してしまうことで<br>自律神経が乱れ、血流が悪くなり、全身に様々な不調をもたらします。</p>
    <p>頭ほぐし専門店 soyo では、そんなお客様のために脳疲労を解消し、<br>全身を整えることを目標とした、水を使用しない<span class="mark">ドライヘッドスパ</span>専門店です。</p>
    <p class="closing">ぜひ、心身の疲れを癒しにお越しください。</p>
  </section>
</main>
</body>
</html>
```